High Profile Wordpress Design for Marketing Agency

http://www.LanternCo.example.nz is moving from GridPortal to wordpress

Lantern Co is a leading New Zealand consumer brands public relations and advertising agency.
Our marketing agency represents some of the worlds most recognisable brands as well as some small independent businesses and everything in between.
Our GPL current site has served us well for 6+ years but we are now wanting to move to wordpress.

We are looking for a new look for our website which will be either a 2013 facelift keeping existing colour scheme rather than a radical new design
Our target market is marketing managers and brand owners familiar with design and marketing elements.
First and foremost the site must be functional from an SEO and loading speed point of view. To assist this we want to retain the text content.
Secondly we have historically had only pointers to other pages on our site but we want to incorporate more of the highlights of our services and our portfolio with the addition of some 'sample boxes' such as in this template: http://vendorplace.example/item/sample-business-theme/full_screen_preview/5821307

Wordpress offers an easier interface for uploading news items which we do daily and also take advantage of the plugins for seo. We are looking to redesign the look of the site while keeping all the existing text content.

Logo – also needs refreshing. Something corporate but not staid. Modern and clean.

Existing pages
- We want a fresh new clean look while retaining the orange and gray colours. white space is good. modern fonts are good.
- Social media : we want to focus on Google Plus primarily but also facebook and twitter. We suggest a funky design with the social media logos. Social media logos on all pages.
- Add New page: client coverage. A page to showcase new client coverage. Could be print, links to online video, mepgs, etc. Perhaps as a blog?
- Add New page: Advertising (as a service).

Home page. Perhaps a larger image existing image can be used or something new that says Stand out from the crowd (but not in a clichéd way). perhaps 3-4 main images could be used which rotate? We want to use stunning image(s) on the site.
Retain existing body of text somewhere on page.

an alternative idea might be to look at images which relate to news. and use the phrase "journalists reaching journalists"

Add Small ‘boxes’ on home page – teasers for content inside the site:
- Our clients logo box. Perhaps use a mouse over to ‘roll’ logos from homepage? Plus link to our clients page. http://www.lanternco.example.nz/OurClients/CurrentClients.aspx
- Our services
- Quotes about us. Show an image of Harbourline magazine with quote about us
- Advertising box: Featured project (as embedded youtube clip and link case study)
- Contact us page – refresh look simple details only.

Client News (blog) page:

Image(s) to top right rather than bottom.
Google Plus like one and share as first icon. Also facebook, twitter share and RSS. (moving icons which scroll down as reader moves down?)

Hi Budget on this project to redesign Auckland PR Firm Lantern Co's website in wordpress has been increased significantly to A$2190

Target Market(s)

Marketing managers, small - large business owners
we are primarily a public relations firm, then advertising. focus should be on these services rather than web design/seo etc which are a secondary part of our offering.

Industry/Entity Type

Advertising

Requirements
Must have
• must retain existing text content(for seo reasons)
fast loading, free of slow graphics
mobile/tablet friendly
new logo
Google Plus 1 logo
Should not have
• our agency is slightly on the conservative side and yet we are looking for a modern look.
prefer light over dark colour scheme/images
Images – better to not use people in images. people from stock images tend to give the impression of an international site and we are looking closer to NZ

```html
<!DOCTYPE html>
<html lang="en">
<head>
<meta charset="utf-8">
<title>Lantern Co – Public Relations &amp; Advertising</title>
<link href="https://fonts.googleapis.com/css2?family=Roboto+Condensed:wght@300;400&family=Source+Sans+3:wght@400;600&display=swap" rel="stylesheet">
<style>
:root{
  --orange:#f7862b;
  --orange-deep:#e8661a;
  --grey-dark:#555;
  --grey:#777;
  --grey-light:#e8e8e8;
  --rule:#d8d8d8;
  --text:#333;
  --white:#fff;
}
*{box-sizing:border-box;margin:0;padding:0}
html,body{width:1144px;height:1200px;overflow:hidden;background:var(--white)}
body{font-family:"Source Sans 3",Arial,sans-serif;color:var(--text)}
.page{position:relative;width:1400px;height:1470px;transform:scale(.81714);transform-origin:0 0}
.abs{position:absolute}
.heading{font-family:"Roboto Condensed",Arial Narrow,sans-serif;font-weight:400;font-size:22px;color:var(--grey);text-transform:uppercase;letter-spacing:.2px}
.heading span{color:var(--orange)}
.btn{position:absolute;display:flex;align-items:center;justify-content:center;gap:4px;background:var(--orange);color:var(--white);font-size:10px;font-weight:600;width:80px;height:23px;letter-spacing:-.2px}
.btn svg{width:10px;height:8px}
.copy{font-size:10.5px;line-height:18px;color:var(--text)}
.rule{position:absolute;left:210px;width:980px;height:1px;background:var(--rule)}
.media{background:linear-gradient(135deg,#cfd6de,#8c98a6)}

/* header */
.logo{left:212px;top:30px;font-family:"Roboto Condensed",sans-serif;font-weight:300;font-size:38px;letter-spacing:18px;color:var(--grey-dark)}
.logo span{color:#a9b3bb}
.search{left:878px;top:44px;width:222px;height:23px;border:1px solid #ccc;font-size:9px;color:var(--grey);padding:6px 10px}
.search svg{position:absolute;right:6px;top:5px}
.login{left:1110px;top:44px;width:80px}
.nav{left:210px;top:89px;width:980px;height:41px;background:var(--orange);display:flex;align-items:center;font-size:11.5px;color:var(--white)}
.nav a{flex:1;text-align:center}
.nav .current{flex:0 0 90px;background:var(--grey-light);color:var(--grey-dark);height:41px;line-height:41px}

/* hero */
.hero{left:210px;top:140px;width:980px;height:374px;background:linear-gradient(90deg,#c9a98a 0%,#efe9e2 35%,#e8ecf0 60%,#dfe4ea 80%,#a9b1ba 100%)}
.hero-band{left:0;top:270px;width:590px;height:74px;background:rgba(200,200,200,.75)}
.hero-title{left:60px;top:280px;font-family:"Roboto Condensed",sans-serif;font-size:46px;color:#333;letter-spacing:-.5px}
.hero-title span{color:var(--orange-deep)}
.dots{right:10px;bottom:10px;display:flex;gap:4px}
.dots i{width:10px;height:10px;background:#f3f3f3;display:block}
.dots i:first-child{background:var(--orange)}

/* client news */
.news-label{left:230px;top:540px}
.brace{left:358px;top:530px;font-family:"Roboto Condensed",sans-serif;font-weight:300;font-size:40px;color:var(--grey)}
.ticker{left:385px;top:546px;font-size:10px;color:#222}

/* services */
.service{position:absolute;top:616px;width:290px;height:130px}
.service .heading{position:absolute;left:0;top:0}
.service .icon{position:absolute;left:0;top:34px;width:56px;height:64px;border-radius:8px}
.service .copy{position:absolute;left:64px;top:40px;width:218px}
.service .btn{left:200px;top:104px}
.divider{position:absolute;top:638px;width:1px;height:98px;background:var(--rule)}
.arrow-nav{left:1140px;top:600px;display:flex;gap:6px}
.shadow{left:225px;top:766px;width:950px;height:4px;background:radial-gradient(ellipse at center,rgba(0,0,0,.15),transparent 70%)}

/* features */
.feature{position:absolute;top:796px}
.frame{position:absolute;border:4px solid #eee}
.about .copy{text-align:justify;width:382px}

/* promo row */
.portfolio{left:210px;top:1122px;width:374px;height:120px;border:1px solid #ddd;background:linear-gradient(90deg,#f7f7f7 0%,#f9d8bc 45%,var(--orange) 75%)}
.portfolio h3{position:absolute;left:198px;top:12px;font-family:"Roboto Condensed",sans-serif;font-weight:400;font-size:24px;color:var(--white)}
.portfolio p{position:absolute;left:199px;top:44px;width:168px;font-size:10.5px;line-height:15px;color:var(--white)}
.portfolio .btn{left:198px;top:80px;background:var(--white);color:var(--orange)}
.portfolio .art{position:absolute;left:10px;top:8px;width:170px;height:100px;border-radius:6px;background:linear-gradient(135deg,#f2f2f2,#dcdcdc)}
.field{left:615px;top:1186px;width:246px;height:24px;border:1px solid #ccc;font-size:8.5px;color:var(--grey);padding:7px 9px}
.contact{left:887px;top:1121px;width:301px;height:124px;background:linear-gradient(90deg,#e9e9e9,#f2f2f2 55%,#cfcfcf)}
.contact .photo{position:absolute;right:0;top:0;width:130px;height:124px;background:linear-gradient(90deg,rgba(240,240,240,0),#b9b9b9)}
.contact .line{position:absolute;left:20px;font-size:11.5px;color:#222}

/* clients */
.clients{left:426px;top:1300px;width:764px;height:50px;display:flex;justify-content:space-between;align-items:center}
.clients span{font-family:"Source Sans 3",sans-serif;font-weight:600;font-size:22px;color:#b8b8b8}

/* footer */
.footer-links{left:212px;top:1393px;font-size:9.5px;color:var(--grey);word-spacing:2px}
.footer-links b{font-weight:400;margin:0 20px;color:#999}
.copyright{left:212px;top:1414px;font-size:9px;color:var(--grey)}
.copyright span{color:var(--orange)}
.follow{left:1010px;top:1406px;font-size:9px;color:var(--orange);font-weight:600}
.social{left:1071px;top:1396px;display:flex;gap:4px}
.social i{display:block;width:26px;height:26px;border-radius:4px;background:linear-gradient(#c4c4c4,#8f8f8f)}
</style>
</head>
<body>
<div class="page">

  <!-- header -->
  <div class="abs logo">LANTERN<span>CO</span></div>
  <div class="abs search">SEARCH :
    <svg width="14" height="14" viewBox="0 0 14 14"><circle cx="5.5" cy="5.5" r="4" fill="none" stroke="#999" stroke-width="1.5"/><line x1="8.5" y1="8.5" x2="13" y2="13" stroke="#999" stroke-width="2"/></svg>
  </div>
  <div class="btn login">LOGIN&nbsp;
    <svg viewBox="0 0 10 8"><path d="M1 0l4 3 4-3M1 4l4 3 4-3" fill="none" stroke="#fff" stroke-width="1.5"/></svg>
  </div>
  <nav class="abs nav">
    <a class="current">HOME</a><a>OUR SERVICES</a><a>NEWS</a><a>OUR PEOPLE</a><a>CASE STUDIES</a><a>OUR CLIENTS</a><a>CONTACT US</a>
  </nav>

  <!-- hero -->
  <section class="abs hero" role="img" aria-label="Banner photograph of smiling business professionals in conversation">
    <div class="abs hero-band"></div>
    <h1 class="abs hero-title"><span>STAND OUT</span> FROM THE CROWD</h1>
    <div class="abs dots"><i></i><i></i><i></i><i></i><i></i></div>
  </section>

  <!-- client news -->
  <h2 class="abs heading news-label"><span>CLIENTS</span> NEWS</h2>
  <div class="abs brace">{</div>
  <p class="abs ticker">MEDIA RELEASE; A NEW BARBECUE AT HOME AND A TRIP FOR TWO TO QUEENSTOWN, TESSA MARLOW ALL SET AFTER WINNING WITH HEARTHMARK</p>
  <a class="btn" style="left:1110px;top:539px">READ MORE <svg viewBox="0 0 10 8"><path d="M0 1l3 3-3 3M5 1l3 3-3 3" fill="none" stroke="#fff" stroke-width="1.6"/></svg></a>
  <div class="rule" style="top:582px"></div>

  <!-- services -->
  <div class="abs arrow-nav">
    <svg width="17" height="17" viewBox="0 0 17 17"><circle cx="8.5" cy="8.5" r="7.5" fill="#f4f4f4" stroke="#999"/><path d="M10 5l-3.5 3.5L10 12" fill="none" stroke="#333" stroke-width="1.6"/></svg>
    <svg width="17" height="17" viewBox="0 0 17 17"><circle cx="8.5" cy="8.5" r="7.5" fill="#f4f4f4" stroke="#999"/><path d="M7 5l3.5 3.5L7 12" fill="none" stroke="#333" stroke-width="1.6"/></svg>
  </div>
  <article class="service" style="left:230px">
    <h3 class="heading"><span>WEB</span> DESIGN</h3>
    <div class="icon media" role="img" aria-label="Illustration of a pot of coloured pencils"></div>
    <p class="copy">Web design is all about presenting content in a unique way online. Lantern Co offers winning creative web design services for your brand.</p>
    <a class="btn">READ MORE <svg viewBox="0 0 10 8"><path d="M0 1l3 3-3 3M5 1l3 3-3 3" fill="none" stroke="#fff" stroke-width="1.6"/></svg></a>
  </article>
  <div class="divider" style="left:530px"></div>
  <article class="service" style="left:560px">
    <h3 class="heading"><span>SOCIAL</span> MEDIA</h3>
    <div class="icon media" style="left:-12px" role="img" aria-label="Illustration of two figures representing a community"></div>
    <p class="copy">The growing online trend towards use of social media by businesses to build their online presence is recognition that these new media.</p>
    <a class="btn">READ MORE <svg viewBox="0 0 10 8"><path d="M0 1l3 3-3 3M5 1l3 3-3 3" fill="none" stroke="#fff" stroke-width="1.6"/></svg></a>
  </article>
  <div class="divider" style="left:860px"></div>
  <article class="service" style="left:890px">
    <h3 class="heading"><span>MEDIA</span> TRAINING</h3>
    <div class="icon media" style="left:-10px;width:64px" role="img" aria-label="Illustration of a retro television set"></div>
    <p class="copy">Perceptions of people, companies and products can be made or broken through a single media appearance.</p>
    <a class="btn">READ MORE <svg viewBox="0 0 10 8"><path d="M0 1l3 3-3 3M5 1l3 3-3 3" fill="none" stroke="#fff" stroke-width="1.6"/></svg></a>
  </article>
  <div class="abs shadow"></div>

  <!-- features -->
  <section class="feature about" style="left:211px">
    <h2 class="heading"><span>ABOUT</span> LANTERN CO</h2>
    <p class="copy" style="margin-top:18px">Our experienced public relations specialists bring together a wealth of experience in public relations (PR), market research, magazines, FMCG / food and beverage marketing, television, and editorial journalism. We help our clients get closer to the mind of their target customer than they have ever been before.</p>
    <p class="copy" style="margin-top:18px">At Lantern Co, our marketing &amp; communications experts will work closely with you as your New Zealand public relations firm and if required, even as your advertising agency. Unlike many other public relations companies we also plan and buy media – however one of our key points of difference is our ability to enhance your brand equity by integrating your TV, print or digital marketing spend with an effective public relations strategy.</p>
  </section>
  <a class="btn" style="left:514px;top:1050px">READ MORE <svg viewBox="0 0 10 8"><path d="M0 1l3 3-3 3M5 1l3 3-3 3" fill="none" stroke="#fff" stroke-width="1.6"/></svg></a>

  <section class="feature" style="left:628px">
    <h2 class="heading"><span>OUR</span> PEOPLE</h2>
  </section>
  <div class="frame media" style="left:625px;top:835px;width:253px;height:105px;background:linear-gradient(180deg,#6d7e90,#2f3a48)" role="img" aria-label="Photograph of the consultant team in business suits"></div>
  <p class="abs copy" style="left:629px;top:951px;width:256px">Lantern Co is a dedicated Auckland advertising and PR agency with an enviable reputation for delivering impressive results. We take your firm's marketing objectives seriously - that is why only the most experienced senior consultants work on your business.</p>
  <a class="btn" style="left:802px;top:1050px">READ MORE <svg viewBox="0 0 10 8"><path d="M0 1l3 3-3 3M5 1l3 3-3 3" fill="none" stroke="#fff" stroke-width="1.6"/></svg></a>

  <section class="feature" style="left:918px">
    <h2 class="heading"><span>CASE</span> STUDIES</h2>
  </section>
  <div class="frame" style="left:915px;top:835px;width:253px;height:105px;background:linear-gradient(90deg,#e4d3c8,#fafafa 40%,#fff)" role="img" aria-label="Photograph of a hand sketching a flow chart on glass"></div>
  <p class="abs copy" style="left:919px;top:951px;width:258px">Our brief was to give a new piece of melanoma research presented at an American Dermatological conference relevance to Australians and New Zealanders. The seminal US research identified six factors that helped predict the risk of developing skin cancer.</p>
  <a class="btn" style="left:1092px;top:1050px">READ MORE <svg viewBox="0 0 10 8"><path d="M0 1l3 3-3 3M5 1l3 3-3 3" fill="none" stroke="#fff" stroke-width="1.6"/></svg></a>

  <div class="rule" style="top:1093px"></div>

  <!-- promo row -->
  <section class="abs portfolio">
    <div class="art" role="img" aria-label="Illustration of a figure lying with a laptop"></div>
    <h3>OUR PORTFOLIO</h3>
    <p>Lantern Co is a dedicated Auckland advertising and PR agency.</p>
    <a class="btn">READ MORE <svg viewBox="0 0 10 8"><path d="M0 1l3 3-3 3M5 1l3 3-3 3" fill="none" stroke="#f7862b" stroke-width="1.6"/></svg></a>
  </section>

  <h2 class="abs heading" style="left:615px;top:1124px"><span>NEWS</span> LETTER</h2>
  <p class="abs" style="left:615px;top:1161px;font-size:11px;color:var(--grey)">GET REGULAR UPDATES FROM <span style="color:var(--orange)">LANTERN CO</span></p>
  <div class="abs field">ENTER YOUR EMAIL ID:</div>
  <a class="btn" style="left:782px;top:1218px">SUBMIT <svg viewBox="0 0 10 8"><path d="M0 1l3 3-3 3M5 1l3 3-3 3" fill="none" stroke="#fff" stroke-width="1.6"/></svg></a>

  <section class="abs contact">
    <div class="photo" role="img" aria-label="Photograph of a thoughtful businessman"></div>
    <h2 class="heading abs" style="left:16px;top:26px"><span>CONTACT</span> US</h2>
    <p class="line" style="top:60px">PHONE : (+649) 555 0148</p>
    <p class="line" style="top:85px">EMAIL: info@lanternco.example.nz</p>
  </section>

  <div class="rule" style="top:1278px"></div>

  <!-- clients -->
  <h2 class="abs heading" style="left:211px;top:1311px;font-size:24px"><span>CURRENT</span> CLIENTS</h2>
  <div class="abs" style="left:401px;top:1290px;width:1px;height:68px;background:var(--rule)"></div>
  <div class="abs clients">
    <span>Brightwell</span><span>Solana</span><span>Dentaro</span><span>Harlow</span><span>Kiwiplay</span><span>Pembrook</span><span>Easel</span>
  </div>

  <div class="rule" style="top:1370px"></div>

  <!-- footer -->
  <nav class="abs footer-links">HOME<b>|</b>OUR SERVICES<b>|</b>NEWS<b>|</b>OUR PEOPLE<b>|</b>CASE STUDIES<b>|</b>OUR CLIENTS<b>|</b>CONTACT US</nav>
  <p class="abs copyright">COPYRIGHT © 2013 <span>LANTERN CO</span>. ALL RIGHTS RESERVED.</p>
  <p class="abs follow">FOLLOW US :</p>
  <div class="abs social" aria-label="Social profiles">
    <i aria-label="Social profile"></i><i aria-label="Social profile"></i><i aria-label="Social profile"></i><i aria-label="News feed"></i>
  </div>

</div>
</body>
</html>
```